Business card design for engineering firm specializing in defense industry.

We need a professional business card design. Something simple but stands out. We are an engineering company specializing in composites in the defense industry.
Industry/Entity Type
Defense
Contact Information for Business Card
A simple black business card with the Varlonix yellow color is what we had in mind but open for other designs.
Colors
ffc214

```html
<!DOCTYPE html>
<html lang="en">
<head>
<meta charset="utf-8">
<title>Varlonix Business Card</title>
<link href="https://fonts.googleapis.com/css2?family=Poppins:wght@400;500;700;800&display=swap" rel="stylesheet">
<style>
  :root {
    --brand-yellow: #ffc214;
    --ink: #0d0d0d;
    --card-black: #0b0b0c;
    --backdrop: #2b2c2f;
    --white: #ffffff;
  }
  * { box-sizing: border-box; margin: 0; padding: 0; }
  html, body {
    width: 1200px; height: 900px; overflow: hidden;
    background: var(--backdrop);
    font-family: 'Poppins', sans-serif;
  }
  .stage {
    width: 1200px; height: 900px;
    display: flex; align-items: center; justify-content: center; gap: 40px;
  }
  .card {
    position: relative; width: 540px; height: 310px;
    border-radius: 26px; overflow: hidden;
    box-shadow: 0 18px 40px rgba(0,0,0,.45);
  }

  /* Front: contact side */
  .card--front { background: var(--brand-yellow); color: var(--ink); }
  .contact { position: absolute; left: 40px; top: 36px; }
  .contact__name { font-weight: 700; font-size: 22px; letter-spacing: -.2px; line-height: 1.1; }
  .contact__role { font-size: 15px; margin-bottom: 14px; }
  .contact__line { display: flex; align-items: center; gap: 10px; font-size: 16px; margin-bottom: 5px; }
  .contact__icon { width: 22px; height: 22px; flex: none; }
  .front__mark {
    position: absolute; right: 70px; top: 78px;
    width: 100px; height: 100px; background: var(--ink);
  }
  .address-band {
    position: absolute; left: 0; right: 0; bottom: 0; height: 78px;
    background: var(--card-black); color: var(--brand-yellow);
    display: flex; align-items: center; padding-left: 40px;
    font-size: 16px;
  }
  .address-band__notch {
    position: absolute; left: 224px; top: -10px;
    width: 0; height: 0;
    border-left: 10px solid transparent; border-right: 10px solid transparent;
    border-bottom: 10px solid var(--card-black);
  }

  /* Back: brand side */
  .card--back {
    background: var(--card-black);
    display: flex; flex-direction: column; align-items: center; justify-content: center; gap: 30px;
  }
  .brand { display: flex; align-items: center; gap: 16px; }
  .brand__square { width: 30px; height: 30px; background: var(--brand-yellow); }
  .brand__name { color: var(--white); font-weight: 800; font-size: 62px; letter-spacing: -1px; line-height: 1; }
  .brand__url {
    color: var(--brand-yellow); font-weight: 700; font-size: 16px;
    letter-spacing: 8px; text-transform: uppercase;
  }
</style>
</head>
<body>
<main class="stage">
  <section class="card card--front">
    <div class="contact">
      <p class="contact__name">MARCUS HALE</p>
      <p class="contact__role">Director</p>
      <p class="contact__line">
        <svg class="contact__icon" viewBox="0 0 24 24" aria-hidden="true"><circle cx="12" cy="12" r="12" fill="#0d0d0d"/><path d="M8.5 6.5l2 2.2-1.2 1.6c.9 1.8 2.2 3.1 4 4l1.6-1.2 2.2 2-1.3 2c-4.3-.3-8.6-4.6-8.9-8.9z" fill="#ffc214"/></svg>
        +420 555 014 272
      </p>
      <p class="contact__line">
        <svg class="contact__icon" viewBox="0 0 24 24" aria-hidden="true"><circle cx="12" cy="12" r="12" fill="#0d0d0d"/><rect x="8" y="5.5" width="8" height="13" rx="1.5" fill="#ffc214"/><rect x="9.3" y="7.3" width="5.4" height="8" fill="#0d0d0d"/></svg>
        +420 555 018 643
      </p>
      <p class="contact__line">
        <svg class="contact__icon" viewBox="0 0 24 24" aria-hidden="true"><circle cx="12" cy="12" r="12" fill="#0d0d0d"/><rect x="6" y="8" width="12" height="8.5" fill="#ffc214"/><path d="M6 8l6 5 6-5" fill="none" stroke="#0d0d0d" stroke-width="1.3"/></svg>
        Enquire@Varlonix.com
      </p>
    </div>
    <div class="front__mark"></div>
    <div class="address-band">
      <span class="address-band__notch"></span>
      Varlonix Works, spol. s r.o. Polní 2207 Brnov 38105, Czech Republic
    </div>
  </section>

  <section class="card card--back">
    <div class="brand">
      <span class="brand__square"></span>
      <span class="brand__name">Varlonix</span>
    </div>
    <p class="brand__url">www.varlonix.com</p>
  </section>
</main>
</body>
</html>
```